High - Class, Very Creative Website needed for Strategic Pricing Consultancy
Cascade Margin Advisory Partners (Tally 9 Yields)
High - Class, Very Creative Website needed for Strategic Pricing Consultancy - Consulting
Creative Brief
Consulting
http://tallyninyields.example/
Cascade Margin Advisory Partners (Tallyridge) is a Strategic Pricing consultancy that specializes in creating and implementing price and profitability strategies that are designed to keep more money in the pockets of business owners. We implement solutions that make sure businesses price intelligently and captures the profits that it deserves. Whether it’s building a brand new pricing strategy, revising existing marketing and pricing tactics, conducting pricing workshops, or providing web based training seminars. We help companies to stop abusing coupons and promotions and to stop overusing "Dealbox" and "Buzzy Savers". We price for profits. Cascade Margin Advisory Partners: Smarter Pricing. Better results.
I like for it to embody cutting-edge, clean, modern and professionalism that this strategic pricing consultancy represents. I don't like bring websites. I want it to jump out and capture potential clients attention while maintaining a professional feel.
Modern
Complex
left side
www.clearview8gain.example
http://brumello.example/
http://www.quorsela.example/
High- class, very creative Website needed for Cascade Margin Advisory Partners. Needs to embody cutting-edge, clean, modern and professionalism that this strategic pricing consultancy represents.

```html
<!DOCTYPE html>
<html lang="en">
<head>
<meta charset="utf-8">
<title>Tallyridge — Clear Pricing for Growth</title>
<link href="https://fonts.googleapis.com/css2?family=Oswald:wght@400;500;700&family=Mulish:ital,wght@0,400;0,600;0,700;0,800;1,400;1,600&display=swap" rel="stylesheet">
<style>
:root{
  --green:#8dc21f;
  --green-band:#9acb1f;
  --navy:#0d3d4f;
  --teal:#0b5d71;
  --teal-dark:#094e60;
  --footer:#0b2a33;
  --footer-bottom:#061d24;
  --ink:#3b3b3b;
  --muted:#5a5a5a;
  --white:#ffffff;
}
*{box-sizing:border-box;margin:0;padding:0}
html,body{width:753px;height:1200px;overflow:hidden}
body{position:relative;font-family:"Mulish",sans-serif;color:var(--ink);background:var(--white)}
.abs{position:absolute}

/* header */
.site-header{left:0;top:0;width:753px;height:62px;background:linear-gradient(#fdfdfd,#eef0f1)}
.brand{left:83px;top:14px}
.brand-name{font-family:"Mulish",sans-serif;font-weight:800;font-size:23px;color:var(--navy);letter-spacing:-.3px;line-height:1}
.brand-tag{font-size:8px;font-weight:600;color:var(--navy);margin-top:4px;margin-left:15px}
.brand-mark{display:inline-block;width:10px;height:10px;background:var(--green);margin-right:5px;vertical-align:middle}
.header-phone{right:82px;top:11px;font-family:"Mulish",sans-serif;font-weight:700;font-size:11px;color:var(--navy);display:flex;align-items:center;gap:5px}
.phone-dot{width:16px;height:16px;border-radius:50%;background:var(--navy);display:flex;align-items:center;justify-content:center}
.main-nav{right:82px;top:35px;display:flex;align-items:center;font-family:"Oswald",sans-serif;font-size:12px;color:#111}
.main-nav a{color:#111;text-decoration:none;padding:0 9px;border-left:1px solid #aaa;line-height:11px}
.main-nav a:last-child{padding-right:0}
.main-nav a.active{background:var(--green);color:#fff;border:none;padding:4px 10px;margin-right:7px;line-height:12px}

/* hero */
.hero{left:0;top:62px;width:753px;height:373px;background:linear-gradient(100deg,#c9ccc9 0%,#e9ebe8 30%,#dfe2e4 55%,#6c7480 75%,#c8a88e 92%,#9a7c68 100%)}
.hero-rule{left:0;top:435px;width:753px;height:3px;background:var(--navy)}
.hero-banner{left:96px;top:260px;width:564px;height:29px;background:linear-gradient(90deg,rgba(11,93,113,.75),rgba(141,194,31,.92) 40%,rgba(141,194,31,.92) 60%,rgba(11,93,113,.75));display:flex;align-items:center;justify-content:center;font-family:"Oswald",sans-serif;color:#fff;font-size:14px;gap:4px}
.hero-banner strong{font-weight:700;font-size:17px}
.hero-banner::after{content:"";position:absolute;left:50%;bottom:-6px;margin-left:-6px;border:6px solid transparent;border-bottom:0;border-top-color:var(--green)}
.service-card{top:319px;width:168px;height:84px;background:rgba(255,255,255,.9);border:1px solid #9aa;border-radius:2px;text-align:center;padding-top:8px}
.service-card svg{display:block;margin:0 auto}
.service-card span{display:block;font-family:"Oswald",sans-serif;font-size:14px;color:var(--navy);margin-top:4px}
.hero-arrow{top:350px}

/* welcome */
.welcome{left:83px;top:462px;width:335px}
.welcome h1{font-weight:400;font-size:12px;color:var(--navy);display:flex;align-items:baseline;gap:6px}
.welcome h1 b{font-weight:800;font-size:18px;color:var(--navy)}
.title-rule{height:1px;background:#ddd;margin-top:4px;position:relative}
.title-rule::before{content:"";position:absolute;left:0;top:-1px;width:68px;height:2px;background:var(--green)}
.welcome h2{font-size:8.6px;font-weight:800;color:var(--navy);margin-top:9px}
.welcome p{font-size:8.6px;line-height:14px;color:var(--muted);margin-top:10px}
.btn-dark{display:inline-block;background:var(--navy);color:#fff;font-weight:800;font-size:7.5px;padding:4px 7px;margin-top:12px;border-radius:1px}
.divider-v{left:440px;top:470px;width:1px;height:120px;background:linear-gradient(transparent,#e3e3e3,transparent)}
.video{left:464px;top:472px;width:207px;height:138px;border:1px solid #333;background:linear-gradient(160deg,#eef1f3,#c9d2d8 60%,#51606e)}
.video-play{left:90px;top:49px;width:33px;height:22px;background:#111;border-radius:4px;display:flex;align-items:center;justify-content:center}
.video-bar{left:0;bottom:0;width:100%;height:20px;background:linear-gradient(#2b2b2b,#111);display:flex;align-items:center;gap:6px;padding:0 6px}
.track{flex:1;height:4px;background:#444;border-radius:2px;position:relative;max-width:112px}
.track i{position:absolute;left:0;top:0;height:4px;width:52px;background:#d23;border-radius:2px}

/* consultancy band */
.specialty{left:0;top:639px;width:753px;height:96px;background:linear-gradient(90deg,var(--teal-dark),var(--teal) 50%,var(--teal-dark))}
.specialty-title{left:84px;top:662px;font-family:"Oswald",sans-serif;font-weight:700;font-size:21px;line-height:25px;color:#fff;letter-spacing:-.2px}
.spec-sep{top:652px;width:1px;height:78px;background:rgba(255,255,255,.15)}
.spec-item{top:648px;width:150px;text-align:center;color:#fff;font-size:11px;line-height:14px}
.spec-circle{width:48px;height:48px;margin:0 auto 6px;border:2px solid #fff;border-radius:50%;display:flex;align-items:center;justify-content:center}

/* lead form */
.lead{left:0;top:735px;width:753px;height:90px;background:var(--green-band)}
.lead h3{position:absolute;left:84px;top:14px;font-family:"Mulish",sans-serif;font-style:italic;font-weight:600;font-size:18px;color:var(--navy)}
.field{top:47px;height:27px;background:#fff;border:1px solid #dfe8c8;font-size:7.5px;color:#888;padding:9px 7px}
.btn-start{left:546px;top:47px;width:124px;height:27px;background:var(--navy);color:#fff;font-weight:800;font-size:13px;display:flex;align-items:center;justify-content:flex-end;padding-right:10px;gap:10px}

/* blog & testimonials */
.section-head{top:845px;display:flex;align-items:center;gap:7px;font-size:16px;color:var(--navy)}
.section-head b{font-weight:800}
.head-rule{top:871px;height:1px;background:#ddd}
.head-rule::before{content:"";position:absolute;left:0;top:-1px;width:62px;height:2px;background:var(--green)}
.pager{top:852px;display:flex;gap:6px}
.post-thumb{left:83px;width:69px;height:58px;border:1px solid #ccc;padding:2px;background:#fff}
.post-thumb div{width:100%;height:100%}
.post-body{left:164px;width:190px}
.post-body a{font-size:7.6px;font-weight:800;color:var(--navy);text-decoration:underline;display:block}
.post-date{font-size:7.3px;color:#6b9b0f;font-weight:700;margin-top:4px}
.post-body p{font-size:7.3px;line-height:11px;color:var(--muted);margin-top:5px}
.post-body p em{font-style:normal;color:var(--green)}
.post-sep{left:83px;top:954px;width:271px;height:1px;border-top:1px dashed #ccc}
.col-sep{left:376px;top:880px;width:1px;height:150px;background:linear-gradient(transparent,#e3e3e3,transparent)}
.avatar{left:399px;top:884px;width:58px;height:58px;border-radius:50%;border:3px solid var(--green);background:#fff;padding:2px}
.avatar div{width:100%;height:100%;border-radius:50%;background:radial-gradient(circle at 50% 40%,#f0d9c8,#c9a68f 60%,#8e7d70)}
.avatar::after{content:"";position:absolute;right:-7px;top:22px;border:5px solid transparent;border-right:0;border-left:6px solid var(--green)}
.client-name{left:472px;top:900px;font-size:9px;font-weight:700;color:var(--navy)}
.client-role{left:472px;top:913px;font-size:7.5px;color:#6b9b0f}
.quote{left:400px;top:965px;width:272px;font-style:italic;font-size:8.2px;line-height:16.3px;color:#666}
.quote b{font-size:18px;color:#c6cdd0;font-style:normal;font-family:Georgia,serif;vertical-align:-4px;line-height:0}

/* footer */
.site-footer{left:0;top:1048px;width:753px;height:128px;background:var(--footer)}
.foot-col{top:1062px;color:#fff}
.foot-col h4{font-size:9.6px;font-weight:700;padding-bottom:5px;border-bottom:1px solid #2a4a55;margin-bottom:7px}
.foot-links li{list-style:none;font-size:7.5px;line-height:16.5px;display:flex;align-items:center;gap:10px}
.foot-links li::before{content:"→";color:var(--green);font-size:8px}
.foot-links li.on{color:var(--green)}
.foot-text{font-size:7.5px;line-height:11.5px;color:#fff}
.foot-vsep{top:1066px;width:1px;height:100px;background:#2a4a55}
.email-field{width:130px;height:16px;background:#fff;border:1px solid #ccc;color:#444;font-size:7.3px;padding:3px 4px;margin-top:13px}
.btn-subscribe{display:inline-block;background:var(--green);color:#fff;font-weight:800;font-size:8.5px;padding:4px 9px;margin-top:11px;border:1px solid #b8e05a}
.foot-brand{left:527px;top:1084px;text-align:center;width:145px}
.foot-brand .brand-name{color:#fff;font-size:21px}
.foot-brand .brand-tag{color:#b9c6cb;margin:4px 0 0 0}
.social{top:1135px;width:18px;height:18px;border-radius:50%;background:#fff}
.copyright{left:0;top:1176px;width:753px;height:24px;background:var(--footer-bottom);color:#c7d0d3;font-size:7.5px;text-align:center;line-height:24px}
</style>
</head>
<body>

<header class="abs site-header">
  <div class="abs brand">
    <div class="brand-name"><span class="brand-mark"></span>Tallyridge</div>
    <div class="brand-tag">Clear Pricing for Growth</div>
  </div>
  <div class="abs header-phone">
    <span class="phone-dot"><svg width="7" height="9" viewBox="0 0 7 9"><rect x="0.5" y="0.5" width="6" height="8" rx="1" fill="none" stroke="#fff"/><rect x="2" y="2" width="3" height="2" fill="#fff"/></svg></span>
    (555)0142-870
  </div>
  <nav class="abs main-nav">
    <a class="active">Home</a><a>Services</a><a>About Us</a><a>Blog</a><a>Contact Us</a>
  </nav>
</header>

<section class="abs hero" role="img" aria-label="Photo of four business people smiling around a meeting table"></section>
<div class="abs hero-banner">We are an Insurance agency <strong>specializing in Pricing consultancy</strong></div>

<svg class="abs hero-arrow" style="left:72px" width="12" height="20" viewBox="0 0 12 20"><path d="M10 2 2 10l8 8" fill="none" stroke="#fff" stroke-width="2.5"/></svg>
<svg class="abs hero-arrow" style="left:670px" width="12" height="20" viewBox="0 0 12 20"><path d="M2 2l8 8-8 8" fill="none" stroke="#fff" stroke-width="2.5"/></svg>

<div class="abs service-card" style="left:100px">
  <svg width="48" height="40" viewBox="0 0 48 40"><rect x="2" y="8" width="44" height="24" rx="2" fill="none" stroke="#7cb518" stroke-width="3"/><circle cx="24" cy="20" r="8" fill="none" stroke="#7cb518" stroke-width="2.5"/><text x="24" y="25" text-anchor="middle" font-family="Oswald,sans-serif" font-weight="700" font-size="13" fill="#7cb518">$</text><path d="M10 3h26l-3-3M38 37H12l3 3" fill="none" stroke="#7cb518" stroke-width="2.5"/></svg>
  <span>Pricing Consultancy</span>
</div>
<div class="abs service-card" style="left:292px">
  <svg width="48" height="40" viewBox="0 0 48 40"><rect x="6" y="14" width="5" height="26" fill="#7cb518"/><circle cx="8.5" cy="9" r="4" fill="#7cb518"/><rect x="18" y="26" width="5" height="14" fill="#7cb518"/><rect x="26" y="22" width="5" height="18" fill="#7cb518"/><rect x="34" y="16" width="5" height="24" fill="#7cb518"/><path d="M16 22l10-8 6 4 10-10" fill="none" stroke="#7cb518" stroke-width="2.5"/><text x="22" y="12" font-family="Oswald,sans-serif" font-weight="700" font-size="12" fill="#7cb518">$</text></svg>
  <span>Profitability Strategies</span>
</div>
<div class="abs service-card" style="left:485px">
  <svg width="48" height="40" viewBox="0 0 48 40"><circle cx="20" cy="17" r="13" fill="none" stroke="#7cb518" stroke-width="3"/><path d="M9 17h6l3-6 4 12 3-6h5" fill="none" stroke="#7cb518" stroke-width="2"/><path d="M30 27l10 10" stroke="#7cb518" stroke-width="5" stroke-linecap="round"/></svg>
  <span>Profit Analysis</span>
</div>
<div class="abs hero-rule"></div>

<section class="abs welcome">
  <h1>Welcome to <b>Tallyridge</b></h1>
  <div class="title-rule"></div>
  <h2>Lorem ipsum dolor sit amet, consectetur adipiscing elit. Nulla in sollicitudin</h2>
  <p>Lorem ipsum dolor sit amet, consectetur adipiscing elit. Nulla in sollicitudin velit, bibendum velit. Cras vel facilisis ipsum, et venenatis risus. In egestas nunc etvb eros auctor sollicitu Etiam ut enim vitae magna volutpat venenatis vitae nonprof diam. Nam nunc velit, tristique a sapien euismod, pulvinar vestibulum dui. Morbi porttitor eu erat imperdiet pretium consequat fcilelis.</p>
  <span class="btn-dark">READ MORE</span>
</section>
<div class="abs divider-v"></div>
<div class="abs video" role="img" aria-label="Video still of three business people shaking hands">
  <div class="abs video-play"><svg width="10" height="11" viewBox="0 0 10 11"><path d="M0 0l10 5.5L0 11z" fill="#fff"/></svg></div>
  <div class="abs video-bar">
    <svg width="7" height="8" viewBox="0 0 7 8"><path d="M0 0l7 4-7 4z" fill="#fff"/></svg>
    <svg width="9" height="8" viewBox="0 0 9 8"><path d="M0 2.5h2L5 0v8L2 5.5H0z" fill="#fff"/><path d="M6.5 2v4M8 1v6" stroke="#fff"/></svg>
    <div class="track"><i></i></div>
    <svg style="margin-left:auto" width="8" height="8" viewBox="0 0 8 8"><path d="M5 0h3v3M3 8H0V5M8 0 5 3M0 8l3-3" fill="none" stroke="#fff"/></svg>
  </div>
</div>

<section class="abs specialty"></section>
<div class="abs specialty-title">WE SPECIALIZING<br>IN CONSULTANCY</div>
<div class="abs spec-sep" style="left:245px"></div>
<div class="abs spec-sep" style="left:385px"></div>
<div class="abs spec-sep" style="left:546px"></div>
<div class="abs spec-item" style="left:238px">
  <div class="spec-circle"><svg width="24" height="24" viewBox="0 0 24 24"><rect x="2" y="6" width="9" height="9" fill="#8dc21f"/><rect x="12" y="6" width="9" height="9" fill="#8dc21f"/><rect x="2" y="16" width="9" height="7" fill="#8dc21f"/><rect x="12" y="16" width="9" height="7" fill="#8dc21f"/></svg></div>
  Marketing and<br>Pricing Tactics
</div>
<div class="abs spec-item" style="left:387px">
  <div class="spec-circle"><svg width="28" height="28" viewBox="0 0 28 28"><circle cx="14" cy="14" r="12" fill="none" stroke="#8dc21f" stroke-width="3"/><text x="14" y="20" text-anchor="middle" font-family="Oswald,sans-serif" font-weight="700" font-size="17" fill="#8dc21f">$</text></svg></div>
  Conducting<br>Pricing Workshops
</div>
<div class="abs spec-item" style="left:546px">
  <div class="spec-circle"><svg width="24" height="26" viewBox="0 0 24 26"><circle cx="12" cy="4" r="3.5" fill="#8dc21f"/><rect x="4" y="9" width="16" height="3" fill="#8dc21f"/><path d="M7 13h10l-2 12H9z" fill="#8dc21f"/></svg></div>
  Web Based<br>Training Seminars
</div>

<section class="abs lead">
  <h3>Are you ready for more profit?</h3>
  <div class="abs field" style="left:83px;width:129px">Name</div>
  <div class="abs field" style="left:224px;width:130px">Email</div>
  <div class="abs field" style="left:366px;width:167px">Message</div>
  <div class="abs btn-start"><svg width="24" height="20" viewBox="0 0 24 20"><path d="M2 19 20 2M14 2h6v6M8 19l8-8" fill="none" stroke="#8dc21f" stroke-width="3"/></svg>Get Started</div>
</section>

<div class="abs section-head" style="left:83px">
  <svg width="24" height="18" viewBox="0 0 24 18"><ellipse cx="10" cy="7" rx="10" ry="7" fill="#8dc21f"/><path d="M4 12l-2 5 6-3z" fill="#8dc21f"/><ellipse cx="16" cy="11" rx="8" ry="5.5" fill="#0d3d4f"/></svg>
  <span>Latest <b>Blog</b></span>
</div>
<div class="abs head-rule" style="left:83px;width:271px"></div>
<div class="abs pager" style="left:337px"><svg width="7" height="12" viewBox="0 0 7 12"><path d="M6 1 1 6l5 5" fill="none" stroke="#999" stroke-width="1.3"/></svg><svg width="7" height="12" viewBox="0 0 7 12"><path d="M1 1l5 5-5 5" fill="none" stroke="#0d3d4f" stroke-width="1.5"/></svg></div>

<div class="abs post-thumb" style="top:884px"><div role="img" aria-label="Hands holding a tablet with glowing network graphics" style="background:linear-gradient(160deg,#1d3a66,#6fa8d8 55%,#0b1a33)"></div></div>
<div class="abs post-body" style="top:886px">
  <a>Ut tellus dolor, dapibus smit dollar nomk egemop</a>
  <div class="post-date">01.01.2015</div>
  <p>Utm tellus dolor, dapibus eget, elemen velmki cursu eleifelitas. Aenean auctorbni wisi et urnam. Aliquam at volutpatis <em>[...]</em></p>
</div>
<div class="abs post-sep"></div>
<div class="abs post-thumb" style="top:966px"><div role="img" aria-label="Blue financial chart with glowing line" style="background:linear-gradient(150deg,#0c2f8a,#2f7de0 50%,#0a2470)"></div></div>
<div class="abs post-body" style="top:968px">
  <a>Ut tellus dolor, dapibus smit dollar nomk egemop</a>
  <div class="post-date">01.01.2015</div>
  <p>Utm tellus dolor, dapibus eget, elemen velmki cursu eleifelitas. Aenean auctorbni wisi et urnam. Aliquam at volutpatis <em>[...]</em></p>
</div>
<div class="abs col-sep"></div>

<div class="abs section-head" style="left:399px">
  <svg width="24" height="20" viewBox="0 0 24 20"><rect x="1.5" y="4.5" width="15" height="14" fill="none" stroke="#8dc21f" stroke-width="2.5"/><path d="M9 13l11-11 3 3-11 11-4 1z" fill="#0d3d4f"/></svg>
  <span>Client <b>Testimonials</b></span>
</div>
<div class="abs head-rule" style="left:399px;width:271px"></div>
<div class="abs pager" style="left:653px"><svg width="7" height="12" viewBox="0 0 7 12"><path d="M6 1 1 6l5 5" fill="none" stroke="#999" stroke-width="1.3"/></svg><svg width="7" height="12" viewBox="0 0 7 12"><path d="M1 1l5 5-5 5" fill="none" stroke="#0d3d4f" stroke-width="1.5"/></svg></div>
<div class="abs avatar"><div role="img" aria-label="Portrait photo of the client"></div></div>
<div class="abs client-name">Mrs. Maribel Strand</div>
<div class="abs client-role">Business Wooman</div>
<p class="abs quote"><b>“</b> Utm tellus dolor, dapibus eget, elemen velmki cursus eleifelita arnean auctorbni wisi et urnam. Lorem ipsum dolor sit amet, conse ctetur adipiscing elit. Nulla in sollicitudin velit, bibendum velit.Cras vel facilisis ipsum, et venenatis risus.</p>

<footer class="abs site-footer"></footer>
<div class="abs foot-col" style="left:83px;width:68px">
  <h4>Quick Links</h4>
  <ul class="foot-links"><li class="on">Home</li><li>Services</li><li>About Us</li><li>Blog</li><li>Contact Us</li></ul>
</div>
<div class="abs foot-vsep" style="left:171px"></div>
<div class="abs foot-col" style="left:193px;width:119px">
  <h4>Contact Detail</h4>
  <div class="foot-text"><b>TALLYRIDGE</b><br>16 Lorem ipsum dolor sit amet sed benetion, Street no-123456</div>
  <div class="foot-text" style="margin-top:12px;display:flex;gap:5px;align-items:center"><svg width="8" height="8" viewBox="0 0 8 8"><path d="M1 0h2l1 2-1 1q1 2 2 2l1-1 2 1v2q-4 1-7-7z" fill="#aab"/></svg>555-014-2233</div>
  <div class="foot-text" style="margin-top:10px;display:flex;gap:5px;align-items:center"><svg width="9" height="7" viewBox="0 0 9 7"><rect width="9" height="7" fill="#aab"/><path d="M0 0l4.5 4L9 0" fill="none" stroke="#0b2a33"/></svg>hello@tallyridge.example</div>
</div>
<div class="abs foot-vsep" style="left:332px"></div>
<div class="abs foot-col" style="left:355px;width:130px">
  <h4>Newsletter Signup</h4>
  <div class="foot-text">Get latest updates by entering your email address</div>
  <div class="email-field">Email Address</div>
  <span class="btn-subscribe">SUBSCRIBE</span>
</div>
<div class="abs foot-vsep" style="left:507px"></div>
<div class="abs foot-brand">
  <div class="brand-name">Tallyridge</div>
  <div class="brand-tag">Clear Pricing for Growth</div>
</div>
<div class="abs social" style="left:555px"></div>
<div class="abs social" style="left:578px"></div>
<div class="abs social" style="left:602px"></div>
<div class="abs social" style="left:625px"></div>
<div class="abs copyright">© 2015 Tallyridge. All Rights Reserved.</div>

</body>
</html>
```